Restaurant Finder Website Design

I need to create a website that will help people find restaurants around a zip code or address.

I would like to have a very clean and simple design. I will need a design for the homepage, that should be very clean and simple to use. its where the users will launch their search. I am thinking something like tavlex like.. big search field with a very clean page where users can create an account or restaurants subscribe to the service.

Also need the design of the search results page, I would like to display a big map with the results and a list on the side or the bottom of the map.

Also need a profile page for the users that sign up to the site.

Mostly what I need are guidelines and color coordinated elements, like a general layout and buttons that work together. I would like to know what the action buttons and elements should look like. Because its going to have some more detail pages.

Target Market(s)

People in general, mainly people that work at an office and have to find a place for lunch every day.

Industry/Entity Type

Restaurant

Number of Pages Required

4 page

Font styles to use
Serif
Sans Serif

Requirements
Must have
• It must be a really simple and clean design but look edgy.

```html
<!DOCTYPE html>
<html lang="en">
<head>
<meta charset="utf-8">
<title>Forkfinder – Find your favorite restaurant</title>
<link rel="stylesheet" href="https://fonts.googleapis.com/css2?family=Gabriela&family=Montserrat:wght@400;600;700&display=swap">
<style>
:root{
  --red:#c8202a;
  --red-dark:#a9161f;
  --ink:#2f2f33;
  --ink-soft:#55565b;
  --white:#ffffff;
  --hero-a:#6b4a33;
  --hero-b:#a7784f;
  --band-a:#5d5955;
  --band-b:#8b8580;
  --dot:#2c2c34;
}
*{box-sizing:border-box;margin:0;padding:0}
html,body{width:1200px;height:3321px;overflow:hidden;background:var(--white)}
body{position:relative;font-family:'Montserrat',Arial,sans-serif;color:var(--ink)}
.abs{position:absolute}
.serif{font-family:'Gabriela',Georgia,serif}
.center{text-align:center}

/* hero */
.hero{left:0;top:0;width:1200px;height:658px;background:linear-gradient(135deg,var(--hero-a),var(--hero-b) 45%,#7a5a3f 70%,#4c3526)}
.hero-shade{left:0;top:0;width:1200px;height:658px;background:rgba(20,15,10,.25)}
.brand{display:flex;align-items:center;gap:10px;color:var(--white);font-size:19px;font-weight:600}
.brand-mark{width:34px;height:34px;border-radius:50%;background:var(--red);border:2px solid var(--white)}
.nav{top:40px;left:608px;display:flex;align-items:center;gap:0;color:var(--white);font-size:14px;font-weight:700}
.nav a{color:inherit;text-decoration:none;margin-right:40px}
.nav .signup{margin:0 0 0 2px;border:2px solid var(--white);border-radius:18px;width:120px;height:34px;display:flex;align-items:center;justify-content:center}
.hero-title{top:236px;left:0;width:1200px;color:var(--white);font-size:44px;line-height:56px}
.search{left:312px;top:399px;width:576px;height:46px;display:flex;background:rgba(255,255,255,.18);border:2px solid rgba(255,255,255,.85)}
.search-field{flex:1;color:var(--white);font-size:13px;font-weight:600;padding-left:30px;display:flex;align-items:center}
.search-btn{width:87px;background:var(--red);display:flex;align-items:center;justify-content:center}

.section-title{left:0;width:1200px;font-size:28px;color:var(--ink)}
.lede{left:0;width:1200px;font-size:13px;line-height:28px;color:var(--ink)}

.step{width:320px;text-align:center}
.step-icon{height:96px;display:flex;justify-content:center;align-items:center}
.step h3{font-family:'Gabriela',Georgia,serif;font-weight:400;font-size:20px;margin-top:24px;color:var(--ink)}
.step p{font-size:10.5px;font-weight:600;line-height:20px;margin:14px auto 0;width:300px;color:var(--ink)}

/* restaurant tiles */
.tile{height:182px;display:flex;flex-direction:column;align-items:center;justify-content:center;color:var(--white)}
.tile .city{font-family:'Gabriela',Georgia,serif;font-size:28px;text-shadow:0 1px 3px rgba(0,0,0,.4)}
.tile .stars{font-size:24px;letter-spacing:4px;margin-top:4px}
.tile .stars .on{color:var(--red)}
.tone-berry{background:linear-gradient(135deg,#4a4b4d,#8c3a2c 45%,#5f6a3a)}
.tone-bread{background:linear-gradient(120deg,#3a3430,#b9a58e 35%,#6b5a44 65%,#c58a3a)}
.tone-olive{background:linear-gradient(135deg,#3b3f3c,#6e7042 40%,#4a2e38 75%,#585a55)}

/* search band */
.band{left:0;top:1904px;width:1200px;height:512px;background:radial-gradient(circle at 40% 55%,#8e4a3f 0,#6a5f58 20%,var(--band-b) 45%,var(--band-a) 100%)}
.band-shade{left:0;top:1904px;width:1200px;height:512px;background:rgba(40,38,36,.25)}
.band-title{color:var(--white)}
.num{width:62px;height:62px;border:2px solid var(--white);border-radius:50%;color:var(--white);font-family:'Gabriela',Georgia,serif;font-size:34px;display:flex;align-items:center;justify-content:center;margin:0 auto}
.band .step,.band-step{color:var(--white)}
.band-step h3{font-family:'Gabriela',Georgia,serif;font-weight:400;font-size:27px;margin-top:10px}
.band-step p{font-size:10.5px;font-weight:600;line-height:20px;margin:12px auto 0;width:300px}

/* press */
.quote-mark{left:0;width:1200px;top:2590px;color:var(--red);font-family:'Gabriela',Georgia,serif;font-size:60px;line-height:60px}
.press-text{left:0;width:1200px;top:2668px;font-family:'Gabriela',Georgia,serif;font-size:16px;line-height:30px;color:var(--ink-soft)}
.press-name{left:0;width:1200px;top:2794px;font-size:20px;font-weight:600;letter-spacing:1px;color:var(--ink)}
.press-url{left:0;width:1200px;top:2828px;font-family:'Gabriela',Georgia,serif;font-size:15px;color:var(--ink-soft)}
.dots{left:570px;top:2893px;display:flex;gap:8px}
.dots span{width:14px;height:14px;border-radius:50%;background:var(--dot)}
.dots span.active{background:var(--red)}

/* footer */
.footer{left:0;top:3004px;width:1200px;height:317px;background:var(--red);color:var(--white)}
.footer-brand{left:0;width:1200px;top:44px;justify-content:center}
.footer-nav{left:0;width:1200px;top:124px;display:flex;justify-content:center;gap:34px;font-size:13px;font-weight:600}
.social{left:0;width:1200px;top:180px;display:flex;justify-content:center;gap:26px}
.social span{width:42px;height:42px;border-radius:50%;background:var(--white)}
.copy{left:0;width:1200px;top:262px;font-family:'Gabriela',Georgia,serif;font-size:12px}
</style>
</head>
<body>

<div class="abs hero" role="img" aria-label="Overhead photo of a wooden table with fries, dips, nachos, toast and drinks"></div>
<div class="abs hero-shade"></div>

<header>
  <div class="abs brand" style="left:160px;top:33px"><span class="brand-mark"></span>Forkfinder</div>
  <nav class="abs nav">
    <a href="#">Home</a><a href="#">Explore</a><a href="#">Pricing</a><a href="#">Blog</a>
    <a href="#" class="signup">Sign up</a>
  </nav>
</header>

<h1 class="abs hero-title serif center" style="font-weight:400">Find your favorite Restaurant<br>with delicious food</h1>
<div class="abs search">
  <div class="search-field">Enter address or ZIP code</div>
  <div class="search-btn">
    <svg width="26" height="26" viewBox="0 0 26 26" fill="none" stroke="#fff" stroke-width="2.4"><circle cx="11" cy="11" r="8"/><line x1="17" y1="17" x2="23" y2="23"/></svg>
  </div>
</div>

<h2 class="abs section-title serif center" style="top:752px;font-weight:400">How Forkfinder work</h2>
<p class="abs lede center" style="top:810px">Lorem ipsum dolor sit amet, consectetur adipiscing elit.<br>Vestibulum gravida suscipit sodales.</p>

<div class="abs step" style="left:137px;top:948px">
  <div class="step-icon">
    <svg width="96" height="96" viewBox="0 0 96 96" fill="none" stroke="#c8202a" stroke-width="3"><circle cx="48" cy="48" r="45"/><circle cx="48" cy="38" r="14"/><path d="M22 80c4-16 14-24 26-24s22 8 26 24"/></svg>
  </div>
  <h3>Create Your Account</h3>
  <p>Sed ut perspiciatis unde omnis iste natus error sit voluptatem accusantium doloremque laudantium, totam rem aperiam.</p>
</div>
<div class="abs step" style="left:438px;top:948px">
  <div class="step-icon">
    <svg width="96" height="80" viewBox="0 0 96 80" fill="none" stroke="#c8202a" stroke-width="3"><rect x="2" y="2" width="92" height="76"/><circle cx="68" cy="24" r="7"/><path d="M6 66l26-26 22 20 12-10 24 18"/></svg>
  </div>
  <h3>Add Photos and Details</h3>
  <p>Sed ut perspiciatis unde omnis iste natus error sit voluptatem accusantium doloremque laudantium, totam rem aperiam.</p>
</div>
<div class="abs step" style="left:739px;top:948px">
  <div class="step-icon">
    <svg width="96" height="96" viewBox="0 0 96 96" fill="none" stroke="#c8202a" stroke-width="3"><path d="M48 78C30 56 22 44 22 32a26 26 0 0 1 52 0c0 12-8 24-26 46z"/><circle cx="48" cy="32" r="9"/><ellipse cx="48" cy="84" rx="38" ry="9"/></svg>
  </div>
  <h3>Get Descovered by People</h3>
  <p>Sed ut perspiciatis unde omnis iste natus error sit voluptatem accusantium doloremque laudantium, totam rem aperiam.</p>
</div>

<h2 class="abs section-title serif center" style="top:1292px;font-weight:400">Top-rated restaurants near you</h2>

<div class="abs tile tone-berry" style="left:162px;top:1386px;width:201px" role="img" aria-label="Photo of roasted tomatoes and greens">
  <span class="city">London</span><span class="stars"><span class="on">★★★★</span>★</span></div>
<div class="abs tile tone-bread" style="left:387px;top:1386px;width:426px" role="img" aria-label="Photo of a sandwich on a plate">
  <span class="city">Paris</span><span class="stars"><span class="on">★★★★</span>★</span></div>
<div class="abs tile tone-olive" style="left:837px;top:1386px;width:201px" role="img" aria-label="Photo of a bowl of olives">
  <span class="city">Madrid</span><span class="stars"><span class="on">★★★★</span>★</span></div>
<div class="abs tile tone-berry" style="left:162px;top:1585px;width:201px" role="img" aria-label="Photo of roasted tomatoes and greens">
  <span class="city">London</span><span class="stars"><span class="on">★★★★</span>★</span></div>
<div class="abs tile tone-olive" style="left:387px;top:1585px;width:202px" role="img" aria-label="Photo of a bowl of olives">
  <span class="city">Madrid</span><span class="stars"><span class="on">★★★★</span>★</span></div>
<div class="abs tile tone-bread" style="left:611px;top:1585px;width:427px" role="img" aria-label="Photo of a sandwich on a plate">
  <span class="city">Paris</span><span class="stars"><span class="on">★★★★</span>★</span></div>

<div class="abs band" role="img" aria-label="Blurred photo of a cherry tomato and lettuce on a fork"></div>
<div class="abs band-shade"></div>
<h2 class="abs section-title band-title serif center" style="top:1988px;font-weight:400;color:#fff">Quick and Easy Search</h2>

<div class="abs step band-step" style="left:137px;top:2110px">
  <div class="num">1</div><h3>Choose a Category</h3>
  <p>Sed ut perspiciatis unde omnis iste natus error sit voluptatem accusantium doloremque laudantium, totam rem aperiam.</p>
</div>
<div class="abs step band-step" style="left:438px;top:2110px">
  <div class="num">2</div><h3>Find Locations</h3>
  <p>Sed ut perspiciatis unde omnis iste natus error sit voluptatem accusantium doloremque laudantium, totam rem aperiam.</p>
</div>
<div class="abs step band-step" style="left:739px;top:2110px">
  <div class="num">3</div><h3>Go Have Fun</h3>
  <p>Sed ut perspiciatis unde omnis iste natus error sit voluptatem accusantium doloremque laudantium, totam rem aperiam.</p>
</div>

<h2 class="abs section-title serif center" style="top:2508px;font-weight:400">What the press says</h2>
<div class="abs quote-mark center">“</div>
<p class="abs press-text center">Lorem ipsum dolor sit amet, consectetur adipiscing elit. Aliquam convallis viverra feugiat.<br>Praesent id ipsum neque. Fusce lorem lorem, finibus ullamcorper vulputate varius,<br>pellentesque id tortor.</p>
<div class="abs press-name center">THE DAILY LEDGER</div>
<div class="abs press-url center">www.website.com</div>
<div class="abs dots"><span></span><span></span><span class="active"></span></div>

<footer class="abs footer">
  <div class="abs brand footer-brand"><span class="brand-mark"></span>Forkfinder</div>
  <nav class="abs footer-nav"><span>Home</span><span>Explore</span><span>Pricing</span><span>Blog</span><span>Sign Up</span></nav>
  <div class="abs social" aria-label="Social links"><span></span><span></span><span></span><span></span><span></span></div>
  <div class="abs copy center">© 2016 Pizza Restaurant</div>
</footer>

</body>
</html>
```